Outdoor Company Business Card design

We are an outdoor adventure company needing a business card. We sell outdoor adventures and clothing. Please use our logo in the business card. We are looking for something unique but delivers a clear message as to who we are. Please be creative

Target Market(s)

Outdoor adventures

Industry/Entity Type

Business

Contact Information for Business Card

Business name: TrailBirch If using the logo, no need to have a spot for the name
Owner / CEO: Ross Dalby
Website: TrailBirch.example
Facebook: Facebook.com/TrailBirch
Instagram: @dalby_ross
phone number: 555-304-7192
Email: Dalbycrew@TrailBirch.example

Colors

Designer to choose colors to be used in the design.

Requirements
Must have
• The business card must include the details mentioned above. ie logo, my name, email, facebook, instagram, website, and phone number.
Should not have
• should not be cluttered or look messy

```html
<!DOCTYPE html>
<html lang="en">
<head>
<meta charset="utf-8">
<title>TrailBirch Business Card</title>
<link rel="stylesheet" href="https://fonts.googleapis.com/css2?family=Montserrat:wght@600&family=Roboto+Condensed:wght@700&family=Roboto:wght@400&display=swap">
<style>
  :root {
    --bg: #2b2b2b;
    --paper: #f3f3f3;
    --brand-blue: #0f75bd;
    --brand-orange: #f15a29;
    --ink-grey: #4a4a4a;
    --rule-grey: #8a8a8a;
    --stripe-grey: #a4a5a8;
    --white: #ffffff;
  }
  * { margin: 0; padding: 0; box-sizing: border-box; }
  html, body { width: 1200px; height: 960px; overflow: hidden; }
  body { background: var(--bg); position: relative; font-family: "Roboto", sans-serif; }

  .card { position: absolute; width: 600px; height: 342px; overflow: hidden; }
  .card-front { left: 314px; top: 113px; background: var(--paper); }
  .card-back { left: 311px; top: 472px; background: var(--brand-blue); }

  .brand-name {
    position: absolute; right: 40px; top: 108px;
    font-family: "Montserrat", sans-serif; font-weight: 600;
    font-size: 31px; letter-spacing: 0.5px; color: var(--brand-blue);
    text-transform: uppercase;
  }

  .holder { position: absolute; left: 34px; top: 183px; }
  .holder-name {
    font-family: "Roboto Condensed", sans-serif; font-weight: 700;
    font-size: 22px; color: var(--brand-blue); text-transform: uppercase; line-height: 26px;
  }
  .holder-title {
    font-family: "Roboto Condensed", sans-serif; font-weight: 700;
    font-size: 14px; color: var(--brand-orange); text-transform: uppercase; letter-spacing: 0.3px;
  }
  .rule { position: absolute; left: 34px; right: 40px; top: 233px; height: 1px; background: var(--rule-grey); }

  .contact-list, .social-list { position: absolute; top: 246px; list-style: none; font-size: 14px; color: var(--ink-grey); }
  .contact-list { left: 34px; }
  .contact-list li, .social-list li { height: 19px; display: flex; align-items: center; gap: 8px; }
  .contact-list svg { width: 12px; height: 12px; fill: var(--brand-blue); }
  .social-list { right: 40px; top: 266px; }
  .social-list li { justify-content: flex-end; }
  .social-dot { width: 11px; height: 11px; background: var(--brand-blue); border-radius: 1px; }

  .front-stripe { position: absolute; left: 0; bottom: 0; width: 600px; height: 8px; }

  .back-brand {
    position: absolute; right: 29px; top: 22px; text-align: right;
    color: var(--white);
  }
  .back-brand-name {
    font-family: "Montserrat", sans-serif; font-weight: 600;
    font-size: 32px; text-transform: uppercase; letter-spacing: 0.5px; line-height: 36px;
  }
  .back-brand-url { font-size: 13px; letter-spacing: 3.6px; text-transform: uppercase; }

  .back-artwork {
    position: absolute; left: 0; top: 0; width: 575px; height: 342px;
    background: linear-gradient(160deg, rgba(255,255,255,0.35) 0%, rgba(241,90,41,0.35) 40%, rgba(150,152,156,0.55) 75%, rgba(150,152,156,0.25) 100%);
    clip-path: polygon(0 0, 40% 0, 100% 50%, 100% 100%, 0 100%);
  }
</style>
</head>
<body>
  <section class="card card-front">
    <div class="brand-name">TrailBirch</div>

    <div class="holder">
      <div class="holder-name">Ross Dalby</div>
      <div class="holder-title">Owner / CEO</div>
    </div>
    <div class="rule"></div>

    <ul class="contact-list">
      <li>
        <svg viewBox="0 0 24 24"><path d="M6.6 10.8a15.1 15.1 0 0 0 6.6 6.6l2.2-2.2a1 1 0 0 1 1-.25 11.4 11.4 0 0 0 3.6.57 1 1 0 0 1 1 1V20a1 1 0 0 1-1 1A17 17 0 0 1 3 4a1 1 0 0 1 1-1h3.5a1 1 0 0 1 1 1c0 1.25.2 2.45.57 3.57a1 1 0 0 1-.25 1z"/></svg>
        555-304-7192
      </li>
      <li>
        <svg viewBox="0 0 24 24"><path d="M2 5h20v14H2z M4 7v1l8 5 8-5V7l-8 5z" fill-rule="evenodd"/></svg>
        Dalbycrew@TrailBirch.example
      </li>
      <li>
        <svg viewBox="0 0 24 24"><circle cx="12" cy="12" r="10"/></svg>
        www.TrailBirch.example
      </li>
    </ul>

    <ul class="social-list">
      <li>/TrailBirch <span class="social-dot"></span></li>
      <li>@dalby_ross <span class="social-dot"></span></li>
    </ul>

    <svg class="front-stripe" viewBox="0 0 600 8" preserveAspectRatio="none">
      <rect x="0" y="0" width="396" height="8" fill="var(--brand-blue)"/>
      <polygon points="394,8 397,0 447,0 444,8" fill="var(--brand-orange)"/>
      <polygon points="448,8 451,0 503,0 500,8" fill="var(--stripe-grey)"/>
      <polygon points="504,8 507,0 556,0 553,8" fill="var(--brand-orange)"/>
      <polygon points="557,8 560,0 600,0 600,8" fill="var(--stripe-grey)"/>
    </svg>
  </section>

  <section class="card card-back">
    <div class="back-artwork" role="img" aria-label="Outdoor illustration of an arrowhead, antlers, a fishing hook and a duck"></div>
    <div class="back-brand">
      <div class="back-brand-name">TrailBirch</div>
      <div class="back-brand-url">www.trailbirch.example</div>
    </div>
  </section>
</body>
</html>
```